Brindlewave Systems Website Project

We require a design to revamp and existing website for a company that provides online solutions for small the medium sized businesses including web development, online marketing, social media, online business plans, social media and e-commerce. We are looking to use colours that integrate well with the current logo. Our target market are small to medium sized businesses and individuals looking for a trusted adviser to cover all their online services.
Existing website - www.brindlewavesystems.com.au
Updates
Participation payments added.
Storyboard layout mentioned in brief was not attached in error. It will be uploaded shortly.
Storyboard file added.
Target Market(s)
Revamp of existing website - Looking for a professional design in line with the target market of small to medium businesses
Industry/Entity Type
Business
Requirements
Must have
- Refer the attached storyboard layout for the site design and requirements. Basic header, footer and sidebar are to be the same on every page with the content changing to match the requirements on each page. 8 pages in total
Should not have
- No click here text

```html
<!DOCTYPE html>
<html lang="en">
<head>
<meta charset="utf-8">
<title>Brindlewave Systems</title>
<link rel="stylesheet" href="https://fonts.googleapis.com/css2?family=Ubuntu:wght@400;500;700&family=Arimo:wght@400;700&display=swap">
<style>
:root{
  --green:#7dbf2e;
  --green-dark:#4e9a12;
  --green-text:#5aa51e;
  --lime:#f4f212;
  --ink:#3a3a3a;
  --body:#555;
  --header-top:#6a6a6a;
  --header-bottom:#151515;
  --footer-top:#a6cf1c;
  --footer-bottom:#5d8c12;
  --line:#cfcfcf;
}
*{margin:0;padding:0;box-sizing:border-box}
html,body{width:960px;height:1200px;overflow:hidden}
body{position:relative;background:#fff;font-family:Arimo,Arial,sans-serif;color:var(--body)}
.abs{position:absolute}
.header-band{left:0;top:0;width:960px;height:176px;background:linear-gradient(var(--header-top),#3a3a3a 60%,var(--header-bottom))}
.footer-band{left:0;top:1040px;width:960px;height:160px;background:linear-gradient(var(--footer-top),var(--footer-bottom))}
.brand{left:92px;top:14px;display:flex;align-items:center;gap:10px}
.brand-mark{width:50px;height:50px;border-radius:50%;background:#fff;border:3px solid var(--green)}
.brand-name{font-family:Ubuntu,sans-serif;font-weight:500;font-size:22px;color:#fff;line-height:1.15;letter-spacing:.5px}
.phone{right:80px;top:12px;display:flex;align-items:center;gap:6px;font-family:Ubuntu,sans-serif;font-weight:700;font-size:17px;color:#fff}
.phone-ico{width:22px;height:22px;border-radius:4px;background:var(--green);display:flex;align-items:center;justify-content:center}
.follow{right:84px;top:50px;display:flex;align-items:center;gap:4px;font-family:Ubuntu,sans-serif;font-size:15px;color:#ddd}
.follow span.sq{width:14px;height:14px;border-radius:3px;background:#4a6fb0;margin-left:1px}
.follow span.sq.o{background:#e87a20}.follow span.sq.l{background:#3a9ad9}
.nav{left:521px;top:94px;display:flex;gap:7px}
.nav a{display:block;height:24px;line-height:24px;text-align:center;font-size:10px;color:#333;text-decoration:none;background:linear-gradient(#fff,#ddd);border-radius:6px;position:relative}
.nav a::after{content:"";position:absolute;left:50%;bottom:-5px;margin-left:-5px;border:5px solid transparent;border-top-color:#ddd;border-bottom:0}
.nav a.current{background:linear-gradient(#9ee03a,#4ea514);color:#fff}
.nav a.current::after{border-top-color:#4ea514}
.panel{left:82px;top:136px;width:796px;height:944px;background:#fff;border-radius:6px}
.hero{left:86px;top:140px;width:788px;height:228px;border-radius:5px 5px 0 0;background:var(--green);overflow:hidden}
.hero-photo{left:0;top:0;width:300px;height:228px;background:linear-gradient(90deg,#2f7d12,#6fb53a 70%,var(--green))}
.hero-title{left:300px;top:10px;width:440px;text-align:center;font-weight:700;font-size:44px;line-height:50px;color:#fff;white-space:nowrap}
.hero-title em{font-style:normal;color:var(--lime)}
.hero-sub{left:355px;top:121px;width:330px;text-align:center;font-size:23px;line-height:29.5px;color:#fff}
.shadow-line{height:10px;background:radial-gradient(ellipse at 50% 0,rgba(0,0,0,.22),transparent 70%)}
.service{width:216px}
.service h3{display:flex;align-items:center;gap:6px;font-family:Ubuntu,sans-serif;font-weight:500;font-size:15px;color:var(--green-text);height:34px}
.service .ico{width:28px;height:30px;border-radius:4px;background:linear-gradient(#f6b23a,#e1472a)}
.service p{margin-top:6px;font-size:10px;line-height:14.4px;letter-spacing:.6px;text-align:justify;color:#555}
.div-v{left:340px;top:400px;width:0;height:348px;border-left:1px dashed var(--line)}
.div-h{left:86px;width:512px;height:0;border-top:1px dashed var(--line)}
.projects-title{left:92px;top:800px;display:flex;align-items:center;gap:12px;font-family:Ubuntu,sans-serif;font-weight:500;font-size:17px;color:var(--ink)}
.folder{width:28px;height:26px;border-radius:3px;background:linear-gradient(#f3d37a,#d8a23a)}
.carousel{left:140px;top:872px;width:396px;height:104px;background:linear-gradient(#eceff1,#d9dde0);border-radius:2px}
.arrow{top:908px}
.scroll{left:130px;top:1018px;width:425px;height:16px;border:1px solid #999;border-radius:8px;background:linear-gradient(#fafafa,#d6d6d6)}
.thumb{left:100px;top:1px;width:72px;height:12px;border-radius:6px;background:linear-gradient(#ffe066,#f2a90d)}
.login{left:626px;top:392px;width:233px;height:194px;border:1px solid #e3e3e3;border-radius:6px;background:linear-gradient(#fff,#f6f6f6);overflow:hidden}
.login h2{position:absolute;left:12px;top:12px;font-family:Ubuntu,sans-serif;font-weight:500;font-size:14.5px;color:var(--green-text)}
.login .corner{position:absolute;right:0;top:0;width:74px;height:66px;background:var(--green-dark);clip-path:polygon(0 0,100% 0,100% 100%)}
.field{position:absolute;left:13px;display:flex;align-items:center;font-size:9.5px;color:#777}
.field label{width:60px}
.field span{width:99px;height:16px;border-radius:8px;background:linear-gradient(#d9d9d9,#ececec)}
.login .btn{position:absolute;left:14px;top:159px;width:112px;height:22px;border-radius:11px;background:linear-gradient(#7ec63a,#3f8c12);color:#fff;font-size:11px;line-height:22px;text-align:center}
.feed{left:628px;top:606px;width:230px;height:208px;background:var(--green);border-radius:2px}
.feed-head{position:absolute;left:10px;top:8px;display:flex;align-items:center;gap:8px;font-family:Ubuntu,sans-serif;color:#fff;font-size:14px;line-height:13px}
.feed-head i{width:22px;height:22px;border-radius:50%;background:#fff}
.tweets{position:absolute;left:2px;top:40px;width:226px;height:138px;background:#fff}
.tweet{padding:5px 5px 3px;border-bottom:1px solid #e6e6e6;font-size:9.5px;line-height:11px;color:#222}
.tweet b{font-weight:400;color:var(--green-dark)}
.tweet a{color:var(--green-dark);text-decoration:none}
.tweet small{display:block;font-size:7px;color:var(--green-dark)}
.feed-foot{position:absolute;left:8px;right:8px;top:186px;display:flex;justify-content:space-between;color:#fff;font-size:10px}
.feed-foot strong{font-family:Ubuntu,sans-serif;font-size:12px}
.community{left:628px;top:832px;width:229px;height:208px;border:1px solid #ccc;background:#fff}
.community-head{height:22px;background:#3b5b98;color:#fff;font-family:Ubuntu,sans-serif;font-weight:700;font-size:15px;padding:2px 6px}
.stripes{height:11px;background:repeating-linear-gradient(135deg,#ddd 0 5px,#f4f4f4 5px 10px)}
.members{position:absolute;left:7px;top:40px;display:grid;grid-template-columns:repeat(5,37px);gap:7px}
.members i{height:37px;border:2px solid #eee;background:#c9b7a6}
.members i.blank{background:#dde3ea}
.join{position:absolute;left:9px;top:180px;width:66px;height:18px;border-radius:3px;background:linear-gradient(#ffb340,#f07a10);color:#fff;font-weight:700;font-size:9px;line-height:18px;text-align:center}
.foot-links{list-style:none;font-size:10px;letter-spacing:.8px;color:#fff}
.foot-links li{height:19.3px}
.foot-links li::before{content:"";display:inline-block;margin-right:8px;border:3.5px solid transparent;border-left:4px solid #fff;border-right:0}
.foot-social{left:754px;top:1112px;font-family:Ubuntu,sans-serif;font-size:13px;color:#fff}
.foot-social div{display:flex;align-items:center;gap:7px;height:32px}
.foot-social i{width:20px;height:20px;border-radius:3px;background:#fff;border:2px solid #cfe6f5}
.copyright{left:0;top:1183px;width:960px;text-align:center;font-size:9px;font-weight:700;color:#fff}
</style>
</head>
<body>
<div class="abs header-band"></div>
<div class="abs footer-band"></div>

<div class="abs brand">
  <span class="brand-mark"></span>
  <span class="brand-name">Brindlewave<br>Systems</span>
</div>

<div class="abs phone">
  <span class="phone-ico"><svg width="12" height="12" viewBox="0 0 24 24"><path d="M6.6 10.8c1.4 2.8 3.8 5.1 6.6 6.6l2.2-2.2c.3-.3.7-.4 1-.2 1.1.4 2.3.6 3.6.6.6 0 1 .4 1 1V20c0 .6-.4 1-1 1C10.6 21 3 13.4 3 4c0-.6.4-1 1-1h3.5c.6 0 1 .4 1 1 0 1.3.2 2.5.6 3.6.1.3 0 .7-.2 1z" fill="#fff"/></svg></span>
  0400 318 265
</div>
<div class="abs follow">Follow Now <span class="sq"></span><span class="sq l"></span><span class="sq"></span><span class="sq o"></span></div>

<nav class="abs nav">
  <a class="current" style="width:65px">HOME</a>
  <a style="width:66px">ABOUT</a>
  <a style="width:65px">SERVICES</a>
  <a style="width:66px">PORTFOLIO</a>
  <a style="width:66px">CONTACT</a>
</nav>

<div class="abs panel"></div>

<section class="abs hero">
  <div class="abs hero-photo" role="img" aria-label="Photo of a hand holding a compass against a blurred green background"></div>
  <h1 class="abs hero-title">Make <em>navigating</em> your<br>business online easy</h1>
  <p class="abs hero-sub">We provide ongoing service to ensure we are delivering the best solution for your business</p>
</section>
<div class="abs shadow-line" style="left:120px;top:368px;width:720px"></div>

<div class="abs div-v"></div>
<div class="abs div-h" style="top:514px"></div>
<div class="abs div-h" style="top:638px"></div>

<article class="abs service" style="left:96px;top:390px">
  <h3><span class="ico" role="img" aria-label="Blogs icon illustration"></span>Blogs</h3>
  <p>Lorem Ipsum is simply dummy text of the printing and typesetting industry. Lorem Ipsum.text of the printing and typesetting industry. Lorem Ipsum.</p>
</article>
<article class="abs service" style="left:362px;top:402px">
  <h3><span class="ico" role="img" aria-label="Online business icon illustration"></span>Online Business</h3>
  <p>Lorem Ipsum is simply dummy text of the printing and typesetting industry. Lorem Ipsum.text of the printing and typesetting industry. Lorem Ipsum.</p>
</article>
<article class="abs service" style="left:102px;top:529px">
  <h3><span class="ico" role="img" aria-label="E-commerce icon illustration"></span>E-commerce</h3>
  <p>Lorem Ipsum is simply dummy text of the printing and typesetting industry. Lorem Ipsum.text of the printing and typesetting industry. Lorem Ipsum.</p>
</article>
<article class="abs service" style="left:362px;top:531px">
  <h3><span class="ico" role="img" aria-label="Online marketing icon illustration"></span>Online Marketing</h3>
  <p>Lorem Ipsum is simply dummy text of the printing and typesetting industry. Lorem Ipsum.text of the printing and typesetting industry. Lorem Ipsum.</p>
</article>
<article class="abs service" style="left:102px;top:646px">
  <h3><span class="ico" role="img" aria-label="Social media icon illustration"></span>Social Media</h3>
  <p>Lorem Ipsum is simply dummy text of the printing and typesetting industry. Lorem Ipsum.text of the printing and typesetting industry. Lorem Ipsum.</p>
</article>
<article class="abs service" style="left:362px;top:648px">
  <h3><span class="ico" role="img" aria-label="Web development icon illustration"></span>Web Development</h3>
  <p>Lorem Ipsum is simply dummy text of the printing and typesetting industry. Lorem Ipsum.text of the printing and typesetting industry. Lorem Ipsum.</p>
</article>
<div class="abs shadow-line" style="left:110px;top:758px;width:470px"></div>

<h2 class="abs projects-title"><span class="folder" role="img" aria-label="Folder icon illustration"></span>Recently Completed Projects</h2>
<div class="abs carousel" role="img" aria-label="Carousel of recently completed website screenshots"></div>
<svg class="abs arrow" style="left:110px" width="24" height="20" viewBox="0 0 24 20"><rect width="24" height="20" rx="4" fill="#222"/><path d="M16 4 6 10l10 6z" fill="#fff"/></svg>
<svg class="abs arrow" style="left:548px" width="24" height="20" viewBox="0 0 24 20"><rect width="24" height="20" rx="4" fill="#222"/><path d="M8 4l10 6-10 6z" fill="#fff"/></svg>
<div class="abs scroll">
  <svg class="abs" style="left:4px;top:2px" width="8" height="10"><path d="M7 0 0 5l7 5z" fill="#222"/></svg>
  <div class="abs thumb"></div>
  <svg class="abs" style="right:4px;top:2px" width="8" height="10"><path d="M1 0l7 5-7 5z" fill="#222"/></svg>
</div>

<aside class="abs login">
  <div class="corner" role="img" aria-label="Decorative corner illustration"></div>
  <h2>Secure Client Login</h2>
  <div class="field" style="top:62px"><label>Name :</label><span></span></div>
  <div class="field" style="top:86px"><label>&nbsp;Email:*</label><span></span></div>
  <div class="field" style="top:112px"><label>&nbsp;Phone:*</label><span></span></div>
  <div class="field" style="top:138px"><label>Message:</label><span></span></div>
  <div class="btn">Please Contact me</div>
</aside>

<aside class="abs feed">
  <div class="feed-head"><i></i><span>Brindlewave<br>Systems</span></div>
  <div class="tweets">
    <div class="tweet"><b>ClearLedger</b> Why your accountant could be costing you an arm and a leg <a>lnk.to/Qw7Rt</a><small>yesterday · reply · retweet · favorite</small></div>
    <div class="tweet"><b>ClearLedger</b> Buyers circle as duty calls <a>news.homefeed.com.au/property/re...</a> via <a>@homefeedau</a><small>2 days ago · reply · retweet · favorite</small></div>
    <div class="tweet"><b>ClearLedger</b> Are you eligible for the Payroll Tax Rebate Scheme? Find out here <a>lnk.to/Mk4Pz</a><small>3 days ago · reply · retweet · favorite</small></div>
  </div>
  <div class="feed-foot"><strong>Social feed</strong><span>Join the conversation</span></div>
</aside>

<aside class="abs community">
  <div class="community-head">Community</div>
  <div class="stripes"></div>
  <div class="members" role="img" aria-label="Grid of member profile photos">
    <i style="background:#9aa3ad"></i><i class="blank"></i><i class="blank"></i><i style="background:#a49a84"></i><i style="background:#b9a58f"></i>
    <i style="background:#d79d8a"></i><i style="background:#8e6a52"></i><i style="background:#6f8fb3"></i><i style="background:#5b4a44"></i><i style="background:#9b7456"></i>
    <i style="background:#7a6e72"></i><i style="background:#b79a86"></i><i style="background:#4c3b33"></i><i style="background:#c8a58e"></i><i style="background:#a69d95"></i>
  </div>
  <div class="join">JOIN NOW</div>
</aside>

<ul class="abs foot-links" style="left:92px;top:1100px">
  <li>Web Design and Development</li>
  <li>Search Engine Optimisation</li>
  <li>Online Business Consultants</li>
  <li>Online Marketing</li>
</ul>
<ul class="abs foot-links" style="left:300px;top:1100px">
  <li>Social Media</li>
  <li>E-commerce</li>
  <li>Blogs</li>
</ul>
<div class="abs foot-social">
  <div><i></i>Follow Us</div>
  <div><i></i>Social Feeds</div>
</div>
<p class="abs copyright">© All Rights Reserved Brindlewave Systems 2011</p>
</body>
</html>
```